Corvanta512 Business Card Redesign

I want to create a design for brand new business cards, I need something exceptional for clear plastic business card design. Please do not submit without it being on a clear design. Photos of the various logo versions attached.

```html
<!DOCTYPE html>
<html lang="en">
<head>
<meta charset="UTF-8">
<title>Corvanta512 Business Card</title>
<link rel="stylesheet" href="https://fonts.googleapis.com/css2?family=Inter:wght@400;500;700&display=swap">
<style>
  :root {
    --sky-top: #a8c4e4;
    --sky-mid: #dce5ee;
    --sky-low: #b9c4d3;
    --sky-base: #8e98ab;
    --card-tint-top: rgba(255, 255, 255, 0.52);
    --card-tint-bottom: rgba(240, 245, 252, 0.30);
    --card-edge: rgba(255, 255, 255, 0.75);
    --navy: #3b4868;
    --ink: #1e2435;
    --contact-ink: #414b64;
    --gold: #c2952f;
    --icon-gold: #9a7c3c;
  }
  * { margin: 0; padding: 0; box-sizing: border-box; }
  html, body {
    width: 1200px;
    height: 900px;
    overflow: hidden;
  }
  body {
    font-family: "Inter", sans-serif;
    position: relative;
    background: linear-gradient(180deg,
      var(--sky-top) 0%,
      var(--sky-mid) 32%,
      var(--sky-mid) 44%,
      var(--sky-low) 62%,
      var(--sky-base) 100%);
  }
  .business-card {
    position: absolute;
    left: 279px;
    top: 203px;
    width: 750px;
    height: 427px;
    background: linear-gradient(180deg, var(--card-tint-top) 0%, var(--card-tint-bottom) 100%);
    -webkit-backdrop-filter: blur(6px);
    backdrop-filter: blur(6px);
    border: 1px solid var(--card-edge);
    box-shadow:
      inset 0 1px 0 rgba(255, 255, 255, 0.9),
      0 6px 18px rgba(40, 55, 80, 0.10);
  }
  .brand {
    position: absolute;
    right: 40px;
    top: 47px;
    display: flex;
    align-items: center;
    gap: 16px;
    height: 44px;
  }
  .brand-dot {
    width: 40px;
    height: 40px;
    border-radius: 50%;
    background: var(--navy);
  }
  .brand-name {
    font-size: 36px;
    font-weight: 700;
    color: var(--gold);
    letter-spacing: 0.5px;
  }
  .holder-name {
    position: absolute;
    left: 41px;
    top: 197px;
    font-size: 30px;
    font-weight: 700;
    color: var(--navy);
    letter-spacing: -0.5px;
  }
  .holder-title {
    position: absolute;
    left: 44px;
    top: 236px;
    font-size: 14px;
    font-weight: 500;
    color: var(--gold);
    letter-spacing: 3px;
  }
  .contact-list {
    position: absolute;
    left: 43px;
    top: 273px;
    list-style: none;
  }
  .contact-item {
    display: flex;
    align-items: center;
    gap: 12px;
    height: 31.5px;
    font-size: 19px;
    color: var(--contact-ink);
  }
  .contact-icon {
    width: 20px;
    height: 20px;
    flex: none;
  }
  .coverage-note {
    position: absolute;
    right: 40px;
    top: 325px;
    text-align: right;
    font-size: 15px;
    line-height: 20px;
    color: var(--ink);
  }
</style>
</head>
<body>
  <div class="business-card">
    <div class="brand">
      <span class="brand-dot"></span>
      <span class="brand-name">Corvanta512</span>
    </div>

    <h1 class="holder-name">John Doe</h1>
    <p class="holder-title">TITLE</p>

    <ul class="contact-list">
      <li class="contact-item">
        <svg class="contact-icon" viewBox="0 0 20 20" aria-hidden="true">
          <circle cx="10" cy="10" r="10" fill="var(--icon-gold)"/>
          <path d="M7 5.5c.5-.4 1.1-.3 1.4.2l.8 1.4c.3.5.1 1-.3 1.3l-.5.4c.5 1.1 1.3 1.9 2.4 2.4l.4-.5c.3-.4.8-.6 1.3-.3l1.4.8c.5.3.6.9.2 1.4-.8 1-1.9 1.2-3 .7-2-1-3.6-2.6-4.6-4.6-.5-1.1-.3-2.2.5-3.2z" fill="#fff"/>
        </svg>
        <span>(833) CRVN-512</span>
      </li>
      <li class="contact-item">
        <svg class="contact-icon" viewBox="0 0 20 20" aria-hidden="true">
          <circle cx="10" cy="10" r="10" fill="var(--icon-gold)"/>
          <rect x="5" y="6.5" width="10" height="7" rx="1" fill="none" stroke="#fff" stroke-width="1.3"/>
          <path d="M5.3 7l4.7 3.6L14.7 7" fill="none" stroke="#fff" stroke-width="1.3"/>
        </svg>
        <span>info@corvanta-512.com</span>
      </li>
      <li class="contact-item">
        <svg class="contact-icon" viewBox="0 0 20 20" aria-hidden="true">
          <circle cx="10" cy="10" r="10" fill="var(--icon-gold)"/>
          <circle cx="10" cy="10" r="5" fill="none" stroke="#fff" stroke-width="1.2"/>
          <ellipse cx="10" cy="10" rx="2.2" ry="5" fill="none" stroke="#fff" stroke-width="1.1"/>
          <path d="M5 10h10" stroke="#fff" stroke-width="1.1"/>
        </svg>
        <span>corvanta-512.com</span>
      </li>
    </ul>

    <p class="coverage-note">Serving clients nationwide<br>All 50 states covered</p>
  </div>
</body>
</html>
```